3D Scans and Virtual Tour photography company needs a website

We need a website build that explains what we do, shows some examples of our 3d scans and virtual tours, some stats on why they are important when when selling your home or marketing your business/premises and a contact form to find out more. We need to target both the real estate agents and consumers. The site needs to looks modern, engaging, clean, not lots of text but more pictures and icons. Needs to be mobile friendly. In fact i would build it from the mobile then out.
Updates

Project Deadline Extended
Reason: Hi Team, I have had a couple of requests to extend the Project deadline, which I have now done. I cant push it much more than this as the business is up and running now and I need the website. Looking forward to reviewing the designs.

Target Market(s)

people selling their home and the real estate industry mostly, however any building can be scanned and have a 3d tour

Industry/Entity Type

Photographer

Font styles to use
Sans Serif

Colors
32a6d6
0355a3
33a6d7
85cae6
cee9f5
3176b5

Requirements
Must have
• Our logo
• an example of the 3d scans
• an example of a dollhouse view
• a contact page
• Replace the orange document examples to blue please
• social media links Quillnest Pondlarken Zembol
Nice to have
• some examples of similar companies websites we like
• favourite would be this one hollanbrick (dot com)
• next fav orvantile (dot com au) and brevolux (dot com au)

```html
<!DOCTYPE html>
<html lang="en">
<head>
<meta charset="utf-8">
<title>Brightfold Imagery – 3D Tours</title>
<link href="https://fonts.googleapis.com/css2?family=Lato:wght@300;400;700&family=Montserrat:wght@400;600&display=swap" rel="stylesheet">
<style>
:root{
  --blue:#32a6d6;
  --blue-deep:#0355a3;
  --blue-mid:#3176b5;
  --blue-soft:#85cae6;
  --blue-pale:#cee9f5;
  --ink:#555b61;
  --muted:#9aa0a6;
  --line:#d9dde0;
  --grey-bg:#f1f2f4;
  --slate:#4b545c;
  --slate-dark:#3c434a;
  --white:#ffffff;
}
*{margin:0;padding:0;box-sizing:border-box}
html,body{width:1200px;height:3571px;overflow:hidden}
body{font-family:"Lato",sans-serif;color:var(--ink);background:var(--white);position:relative}
.section{position:absolute;left:0;width:1200px}
.center{text-align:center}
.btn-outline{display:inline-block;border:2px solid #c9ced2;padding:9px 26px;font:600 11px "Montserrat",sans-serif;letter-spacing:1px;color:var(--ink);text-transform:uppercase;background:transparent}

/* header */
.site-header{top:0;height:86px;background:var(--blue)}
.brand{position:absolute;left:155px;top:18px;color:var(--white);font:700 30px "Lato",sans-serif;letter-spacing:1px;line-height:30px}
.brand small{display:block;font:300 19px "Lato",sans-serif;letter-spacing:8px;line-height:22px}
.nav{position:absolute;left:440px;top:32px;display:flex;gap:38px;font:600 11px "Montserrat",sans-serif;color:var(--white);text-transform:uppercase;letter-spacing:.5px}
.nav .active{border-left:2px solid var(--white);border-right:2px solid var(--white);padding:0 12px;margin-left:-14px}
.nav-cta{position:absolute;left:935px;top:24px;width:100px;height:30px;border:2px solid var(--white);color:var(--white);font:600 11px "Montserrat",sans-serif;text-transform:uppercase;display:flex;align-items:center;justify-content:center}

/* hero */
.hero{top:86px;height:433px;background:linear-gradient(90deg,#3a2e28 0%,#6b5a4c 25%,#9a8a7a 45%,#5c4a3c 70%,#2e2620 100%)}
.hero-title{position:absolute;top:155px;width:100%;text-align:center;color:var(--white);font:300 29px/40px "Lato",sans-serif}
.hero-arrow{position:absolute;top:200px}

/* intro */
.intro{top:519px;height:300px}
.intro p{position:absolute;top:62px;width:100%;text-align:center;font:300 19px/26px "Lato",sans-serif;color:#5c6268}
.intro p span{color:var(--blue)}
.intro .btn-outline{position:absolute;top:200px;left:528px;width:144px;text-align:center}

/* how it works */
.how{top:795px;height:288px}
.how h2{position:absolute;top:8px;width:100%;text-align:center;font:300 19px "Lato",sans-serif;color:#5c6268}
.how .rule{position:absolute;top:116px;left:155px;width:890px;height:1px;background:var(--line)}
.step{position:absolute;top:60px;width:200px;text-align:center}
.step .disc{width:114px;height:114px;border-radius:50%;background:var(--blue);margin:0 auto;display:flex;align-items:center;justify-content:center;position:relative;z-index:1}
.step h3{margin-top:10px;font:300 19px "Lato",sans-serif;color:var(--muted)}
.step p{font:300 14px "Lato",sans-serif;color:var(--muted);margin-top:4px}
.gap-label{position:absolute;top:106px;font:400 13px "Lato",sans-serif;color:var(--blue);background:var(--white);padding:0 8px}

/* dollhouse */
.dollhouse{top:1083px;height:441px;background:var(--slate)}
.dollhouse-model{position:absolute;left:190px;top:0;width:820px;height:441px;background:linear-gradient(160deg,#767c80,#5e656b 60%,#4f575e)}
.play{position:absolute;left:559px;top:137px}
.dollhouse h2{position:absolute;top:224px;width:100%;text-align:center;color:var(--white);font:300 27px "Lato",sans-serif}
.view-tabs{position:absolute;top:276px;left:400px;display:flex;gap:12px}
.view-tabs span{width:118px;height:30px;display:flex;align-items:center;justify-content:center;font:600 11px "Montserrat",sans-serif;color:var(--white);border:2px solid #c8ccd0;text-transform:uppercase}
.view-tabs .on{background:var(--blue);border-color:var(--blue)}

/* stats */
.stats{top:1524px;height:321px}
.stat{position:absolute;top:60px;width:260px;text-align:center}
.stat h3{margin-top:12px;font:400 20px "Lato",sans-serif;color:#5c6268}
.stat p{margin-top:4px;font:300 14px/19px "Lato",sans-serif;color:var(--muted)}
.stat p b{color:var(--blue);font-weight:400}
.stats .btn-outline{position:absolute;top:224px;left:528px;width:144px;text-align:center}

/* features */
.features{top:1845px;height:369px;background:var(--grey-bg)}
.features h2{position:absolute;top:55px;width:100%;text-align:center;font:300 19px "Lato",sans-serif;color:#5c6268}
.features h2 span{color:var(--blue)}
.feature{position:absolute;top:110px;width:170px;text-align:center}
.feature .ring{width:100px;height:100px;border-radius:50%;border:2px solid var(--blue);margin:0 auto;display:flex;align-items:center;justify-content:center;background:var(--white)}
.feature .ring.solid{background:var(--blue)}
.feature p{margin-top:14px;font:300 14px/19px "Lato",sans-serif;color:var(--muted)}
.dots{position:absolute;top:304px;left:547px;display:flex;gap:12px}
.dots i{display:block;width:26px;height:3px;background:#b9bec2}
.dots i.on{background:var(--blue)}
.car-arrow{position:absolute;top:158px}

/* listings */
.listings{top:2214px;height:893px;background:linear-gradient(180deg,#5b5e62 0%,#8a8c8f 38%,#d6d7d8 58%,#ffffff 62%)}
.listings h2{position:absolute;top:60px;width:100%;text-align:center;color:var(--white);font:300 27px "Lato",sans-serif}
.listings .sub{position:absolute;top:98px;width:100%;text-align:center;color:var(--white);font:300 14px "Lato",sans-serif}
.partners{position:absolute;top:138px;left:0;width:100%;display:flex;justify-content:center;align-items:center;gap:40px;color:var(--white)}
.partner{display:flex;align-items:center;gap:10px;font:700 26px "Lato",sans-serif}
.partner i{display:block;width:26px;height:26px;background:var(--white)}
.partners .divider{width:1px;height:52px;background:rgba(255,255,255,.6)}
.devices{position:absolute;left:210px;top:238px;width:790px;height:384px;background:linear-gradient(180deg,#e9ecef,#c5cbd1);border-radius:10px}
.book{position:absolute;top:692px;width:100%;text-align:center}
.book h2{font:300 27px "Lato",sans-serif;color:var(--blue)}
.book p{margin-top:10px;font:400 19px "Lato",sans-serif;color:#5c6268}
.social{position:absolute;top:792px;left:525px;display:flex;gap:20px}
.social a{display:block;width:40px;height:40px;border-radius:50%}

/* contact */
.contact{top:3107px;height:464px;background:var(--slate-dark)}
.contact h2{position:absolute;top:64px;width:100%;text-align:center;color:var(--white);font:400 20px "Lato",sans-serif}
.contact .lead{position:absolute;top:98px;width:100%;text-align:center;color:#b8bdc2;font:300 13px/19px "Lato",sans-serif}
.field{position:absolute;height:33px;background:#8a9096;color:#dfe2e5;font:300 12px "Lato",sans-serif;padding:9px 10px}
.send{position:absolute;left:580px;top:308px;width:40px;height:40px;border-radius:50%;background:var(--white);display:flex;align-items:center;justify-content:center}
.copyright{position:absolute;top:392px;width:100%;text-align:center;color:#b8bdc2;font:400 10px "Montserrat",sans-serif;letter-spacing:1px}
</style>
</head>
<body>

<section class="section site-header">
  <div class="brand">brightfold<small>Imagery</small></div>
  <nav class="nav">
    <span class="active">About us</span><span>Service</span><span>3D Tours</span><span>Industries</span><span>Contact</span>
  </nav>
  <div class="nav-cta">Book now</div>
</section>

<section class="section hero" role="img" aria-label="Wide interior photograph of a living room and kitchen with timber floors">
  <h1 class="hero-title">A 3D Tour Allows for Genuine<br>Buyers to Build an Emotional Connection<br>with the Property</h1>
  <svg class="hero-arrow" style="left:108px" width="26" height="18" viewBox="0 0 26 18"><path d="M25 9H2M9 2L2 9l7 7" fill="none" stroke="#fff" stroke-width="2"/></svg>
  <svg class="hero-arrow" style="left:1066px" width="26" height="18" viewBox="0 0 26 18"><path d="M1 9h23M17 2l7 7-7 7" fill="none" stroke="#fff" stroke-width="2"/></svg>
</section>

<section class="section intro">
  <p>Brightfold Imagery <span>provides 3 different viewing</span> perspectives including.<br>A detailed <span>birds eye view</span> with our Floor-plan layouts. A <span>3D experience</span> via our<br><span>Dollhouse View</span> and A first person <span>Virtual reality tour</span>,<br>as if you were physically there.</p>
  <span class="btn-outline">Discover more</span>
</section>

<section class="section how">
  <h2>How it Works ?</h2>
  <div class="rule"></div>
  <span class="gap-label" style="left:425px">2 Hrs</span>
  <span class="gap-label" style="left:722px">48 Hrs</span>
  <div class="step" style="left:196px">
    <div class="disc"><svg width="50" height="40" viewBox="0 0 50 40"><rect x="3" y="9" width="44" height="28" rx="4" fill="none" stroke="#fff" stroke-width="3"/><path d="M17 9l4-6h8l4 6" fill="none" stroke="#fff" stroke-width="3"/><circle cx="25" cy="23" r="8" fill="none" stroke="#fff" stroke-width="3"/></svg></div>
    <h3>Scan</h3><p>Capture a Space in 3D</p>
  </div>
  <div class="step" style="left:500px">
    <div class="disc"><svg width="54" height="44" viewBox="0 0 54 44"><path d="M14 34H11a9 9 0 010-18 14 14 0 0127-3 10 10 0 015 20h-3" fill="none" stroke="#fff" stroke-width="3"/><path d="M27 42V22M20 29l7-7 7 7" fill="none" stroke="#fff" stroke-width="3"/></svg></div>
    <h3>Upload</h3><p>Process &amp; Store in the Cloud</p>
  </div>
  <div class="step" style="left:804px">
    <div class="disc"><svg width="28" height="48" viewBox="0 0 28 48"><rect x="2" y="2" width="24" height="44" rx="4" fill="none" stroke="#fff" stroke-width="3"/><path d="M2 9h24M2 38h24" stroke="#fff" stroke-width="2"/></svg></div>
    <h3>View</h3><p>Experience via Web &amp; Mobile</p>
  </div>
</section>

<section class="section dollhouse">
  <div class="dollhouse-model" role="img" aria-label="Dollhouse cutaway render of a furnished apartment"></div>
  <svg class="play" width="82" height="82" viewBox="0 0 82 82"><circle cx="41" cy="41" r="38" fill="none" stroke="#fff" stroke-width="4"/><path d="M33 26l22 15-22 15z" fill="#fff"/></svg>
  <h2>Stand out onine by attracting the rigth buyers.</h2>
  <div class="view-tabs"><span class="on">Dollhouse</span><span>Floor plan</span><span>First person</span></div>
</section>

<section class="section stats">
  <div class="stat" style="left:155px">
    <svg width="40" height="44" viewBox="0 0 40 44"><path d="M14 6a6 6 0 00-2 0M6 14a8 8 0 0116-4" fill="none" stroke="#32a6d6" stroke-width="2"/><path d="M14 42l-6-14a3 3 0 015-3l4 5V12a3 3 0 016 0v10l9 3c3 1 4 3 4 6l-2 11z" fill="#32a6d6"/></svg>
    <h3>Buyers Love 3D Tours!</h3>
    <p><b>80%</b> increase in enquiries for properties<br>with <b>3D Tours</b></p>
  </div>
  <div class="stat" style="left:470px">
    <svg width="40" height="44" viewBox="0 0 40 44"><circle cx="20" cy="25" r="16" fill="none" stroke="#32a6d6" stroke-width="3"/><path d="M15 3h10M20 3v6M20 25l6-7" stroke="#32a6d6" stroke-width="3" fill="none"/></svg>
    <h3>Online Engagement</h3>
    <p>Users spend <b>52%</b> longer on listings fea-<br>turing <b>3D Tours</b></p>
  </div>
  <div class="stat" style="left:785px">
    <svg width="44" height="44" viewBox="0 0 44 44"><path d="M18 26l8-8M16 20l-6 6a6 6 0 008 8l6-6M28 24l6-6a6 6 0 00-8-8l-6 6" fill="none" stroke="#32a6d6" stroke-width="3" stroke-linecap="round"/></svg>
    <h3>Better Than Video</h3>
    <p><b>3D Tours</b> provide <b>4x</b> engagement com-<br>pared to video</p>
  </div>
  <span class="btn-outline">Get in touch</span>
</section>

<section class="section features">
  <h2>What Sets <span>brightfold imagery</span> apart from the rest</h2>
  <svg class="car-arrow" style="left:114px" width="18" height="12" viewBox="0 0 18 12"><path d="M17 6H2M7 1L2 6l5 5" fill="none" stroke="#c4c8cc" stroke-width="1.5"/></svg>
  <svg class="car-arrow" style="left:1068px" width="18" height="12" viewBox="0 0 18 12"><path d="M1 6h15M11 1l5 5-5 5" fill="none" stroke="#c4c8cc" stroke-width="1.5"/></svg>
  <div class="feature" style="left:172px">
    <div class="ring"><span role="img" aria-label="Small map of Australia" style="display:block;width:48px;height:40px;border-radius:40%;background:var(--blue)"></span></div>
    <p>Australia's Leading 3D tour<br>Provider</p>
  </div>
  <div class="feature" style="left:400px">
    <div class="ring solid"><svg width="46" height="40" viewBox="0 0 46 40"><rect x="2" y="2" width="42" height="36" rx="2" fill="none" stroke="#fff" stroke-width="3"/><path d="M2 11h42" stroke="#fff" stroke-width="3"/><circle cx="8" cy="7" r="1.5" fill="#fff"/><circle cx="13" cy="7" r="1.5" fill="#fff"/><path d="M10 20h26M10 27h18" stroke="#fff" stroke-width="2"/></svg></div>
    <p>Customised branded web<br>players</p>
  </div>
  <div class="feature" style="left:628px">
    <div class="ring"><svg width="44" height="44" viewBox="0 0 44 44"><rect x="3" y="3" width="38" height="38" fill="none" stroke="#32a6d6" stroke-width="3"/><path d="M3 20h16v21M19 3v10M26 20h15M26 20v10" fill="none" stroke="#32a6d6" stroke-width="3"/></svg></div>
    <p>Free floor plans including<br>measurements with every<br>scan</p>
  </div>
  <div class="feature" style="left:856px">
    <div class="ring"><svg width="46" height="42" viewBox="0 0 46 42"><rect x="2" y="2" width="42" height="30" fill="none" stroke="#32a6d6" stroke-width="3"/><path d="M23 32v8M14 40h18" stroke="#32a6d6" stroke-width="3"/><path d="M9 24l9-9 7 6 12-11" fill="none" stroke="#32a6d6" stroke-width="3"/></svg></div>
    <p>Fortnightly analytic reviews<br>lorem ipsum</p>
  </div>
  <div class="dots"><i class="on"></i><i></i><i></i></div>
</section>

<section class="section listings">
  <h2>Stop Buyers in their tracks with an engaging 3D Tour.</h2>
  <p class="sub">Now available on</p>
  <div class="partners">
    <span class="partner"><i></i>Harbourlist</span>
    <span class="divider"></span>
    <span class="partner">Keystead</span>
  </div>
  <div class="devices" role="img" aria-label="Tablet, desktop browser and phone showing a property listing with a 3D tour"></div>
  <div class="book">
    <h2>Book your 3d Tour Today!</h2>
    <p>Call: 1800 555 019 &nbsp;/&nbsp; Email: info@brightfold.com.au</p>
  </div>
  <div class="social">
    <a href="#" aria-label="Quillnest" style="background:#9bb0d0"></a>
    <a href="#" aria-label="Zembol" style="background:var(--blue)"></a>
    <a href="#" aria-label="Pondlarken" style="background:#3c434a"></a>
  </div>
</section>

<section class="section contact">
  <h2>Contact Us</h2>
  <p class="lead">Find ou more about how brightfold can give you a competetive<br>advantage in marketing your property</p>
  <div class="field" style="left:232px;top:166px;width:250px">Name</div>
  <div class="field" style="left:503px;top:166px;width:250px">Email</div>
  <div class="field" style="left:774px;top:166px;width:194px">Phone</div>
  <div class="field" style="left:232px;top:207px;width:736px;height:120px">Type your message ...</div>
  <div class="send"><svg width="18" height="16" viewBox="0 0 18 16"><path d="M1 7L17 1l-4 14-4-5z" fill="#32a6d6"/></svg></div>
  <p class="copyright">© 2017 BRIGHTFOLD</p>
</section>

</body>
</html>
```